New Electrical Business Card Design

I would like a new design for my business cards.
i would like the same logo and font but new design
Please see attached files for front and back design.
large image can be used for graphics.
I would like the instagram link incorporated to back of card.
website site address needs to be changed to www.tidemarkelectrical.au
everything else stays as is

```html
<!DOCTYPE html>
<html lang="en">
<head>
<meta charset="utf-8">
<title>Tidemark Electrical – Business Card</title>
<link href="https://fonts.googleapis.com/css2?family=Arimo:wght@400;700&display=swap" rel="stylesheet">
<style>
  :root {
    --stage: #e4e4e4;
    --card: #231f20;
    --edge: #1f7a3c;
    --green: #1e9a4a;
    --white: #ffffff;
    --grey: #8a8a8a;
    --divider: #6b6b6b;
  }
  * { box-sizing: border-box; margin: 0; padding: 0; }
  html, body {
    width: 1200px; height: 800px; overflow: hidden;
    background: var(--stage);
    font-family: "Arimo", Arial, sans-serif;
  }
  .stage {
    width: 1200px; height: 800px;
    display: flex; align-items: center; justify-content: center; gap: 50px;
  }
  .card {
    position: relative;
    width: 540px; height: 310px;
    background: var(--card);
    border-radius: 22px;
    border: 2px solid var(--edge);
    color: var(--white);
  }

  /* Details side */
  .card-details .brand-dot {
    position: absolute; top: 26px; right: 28px;
    width: 40px; height: 40px; border-radius: 50%;
    background: var(--grey);
  }
  .identity {
    position: absolute; left: 40px; top: 118px;
    width: 250px; text-align: right; padding-right: 18px;
    border-right: 1px solid var(--divider);
  }
  .identity .name {
    color: var(--green); font-weight: 700; font-size: 19px; letter-spacing: 0.5px;
    margin-bottom: 6px;
  }
  .identity .line { font-size: 13px; line-height: 18px; }
  .identity .label { color: var(--green); }
  .contact {
    position: absolute; left: 306px; top: 118px;
    list-style: none; font-size: 13px;
  }
  .contact li { display: flex; align-items: center; gap: 8px; line-height: 21px; }
  .contact svg { width: 12px; height: 12px; fill: var(--green); flex: none; }
  .services {
    position: absolute; left: 0; right: 0; bottom: 40px;
    text-align: center; font-size: 17px; letter-spacing: 0.3px;
  }
  .services .sep { color: var(--green); padding: 0 5px; }

  /* Brand side */
  .card-brand { display: flex; flex-direction: column; align-items: center; justify-content: center; }
  .wordmark {
    font-weight: 700; font-size: 40px; letter-spacing: 1px;
    color: var(--white); text-transform: uppercase;
  }
  .social {
    margin-top: 46px; display: flex; align-items: center; gap: 9px; font-size: 18px;
  }
  .social .mark { width: 16px; height: 16px; border-radius: 50%; background: var(--green); }
</style>
</head>
<body>
<main class="stage">
  <section class="card card-details">
    <span class="brand-dot" aria-hidden="true"></span>
    <div class="identity">
      <p class="name">DANIEL CORVETTI</p>
      <p class="line"><span class="label">ABN</span> - 12 604 887 213</p>
      <p class="line"><span class="label">Lic number</span> - 510834C</p>
    </div>
    <ul class="contact">
      <li>
        <svg viewBox="0 0 24 24" aria-hidden="true"><path d="M6.6 10.8a15.2 15.2 0 0 0 6.6 6.6l2.2-2.2a1 1 0 0 1 1-.25 11.4 11.4 0 0 0 3.6.57 1 1 0 0 1 1 1V20a1 1 0 0 1-1 1A17 17 0 0 1 3 4a1 1 0 0 1 1-1h3.5a1 1 0 0 1 1 1c0 1.25.2 2.45.57 3.57a1 1 0 0 1-.25 1z"/></svg>
        0400 318 552
      </li>
      <li>
        <svg viewBox="0 0 24 24" aria-hidden="true"><path d="M2 5h20v14H2z M2 5l10 8 10-8" stroke="#231f20" stroke-width="1.5"/></svg>
        info@tidemarkelectrical.au
      </li>
      <li>
        <svg viewBox="0 0 24 24" aria-hidden="true"><circle cx="12" cy="12" r="10"/><path d="M2 12h20M12 2c3 3 3 17 0 20M12 2c-3 3-3 17 0 20" stroke="#231f20" stroke-width="1.5" fill="none"/></svg>
        www.tidemarkelectrical.au
      </li>
    </ul>
    <p class="services">Residential<span class="sep">•</span>Commercial<span class="sep">•</span>Industrial<span class="sep">•</span>24hr service</p>
  </section>

  <section class="card card-brand">
    <p class="wordmark">Tidemark Electrical</p>
    <p class="social"><span class="mark" aria-hidden="true"></span>tidemark.electrical</p>
  </section>
</main>
</body>
</html>
```